Online Course Page

We are building a video based online course page. This project is for only the actual page that the student will watch the videos at. They will watch one vide at a time. Once one video lesson is completed then they can move to the next video lesson. The page will need to show the video player. (Main feature.) The list of lessons in the course. Instructor information. Profile picture and bio of the instructor. A Live chat button that will initiate a chat in real-time with the instructor.

The winning designer will also be asked to to design the dashboard area and other aspects of the user interface as an additional project.

Target Market(s)

Adults

Number of Pages Required

1 page

Colors
9bcb3c

Requirements
Must have
• Our logo is attached. Green and grey are our colors. Should feel modern, clean and be simple to navigate. The site will be responsive so the layout should work well on mobile devices.

```html
<!DOCTYPE html>
<html lang="en">
<head>
<meta charset="utf-8">
<title>LearnHarbor – Online Course</title>
<link href="https://fonts.googleapis.com/css2?family=Poppins:wght@400;500;600&family=Roboto+Condensed:wght@400;700&family=Open+Sans:wght@400;600&display=swap" rel="stylesheet">
<style>
:root{
  --green:#8cc43c;
  --green-bright:#9bcb3c;
  --green-deep:#1e4509;
  --ink:#1c1c1c;
  --grey-text:#555;
  --grey-soft:#f1f1f1;
  --topbar:#2a2a2a;
  --white:#fff;
  --black:#050505;
}
*{box-sizing:border-box;margin:0;padding:0}
html,body{width:1200px;height:3846px;overflow:hidden}
body{position:relative;background:var(--white);font-family:"Open Sans",Arial,sans-serif;color:var(--ink)}
.abs{position:absolute}

/* top bar */
.topbar{left:0;top:0;width:1200px;height:41px;background:var(--topbar);color:#ddd;font-size:14px}
.topbar .contact{left:92px;top:11px;display:flex;gap:26px}
.topbar .contact span{display:flex;align-items:center;gap:7px}
.topbar .login{left:882px;top:0;width:118px;height:41px;background:var(--green);color:#fff;font-family:"Poppins",sans-serif;font-size:15px;display:flex;align-items:center;justify-content:center}
.topbar .social{left:1020px;top:12px;display:flex;gap:6px}
.topbar .social i{width:15px;height:15px;background:#fff;border-radius:2px;display:block}

/* header */
.header{left:0;top:41px;width:1200px;height:123px;background:var(--white)}
.brand{left:92px;top:44px;display:flex;align-items:center;gap:12px;font-family:"Poppins",sans-serif;font-weight:600;font-size:30px;color:var(--green-deep)}
.brand b{width:30px;height:30px;border-radius:50%;background:var(--green);display:block}
.nav{left:495px;top:52px;display:flex;gap:42px;font-family:"Poppins",sans-serif;font-size:17px;color:#333}
.nav .active{color:var(--green)}

/* hero */
.hero{left:0;top:164px;width:1200px;height:590px;background:linear-gradient(100deg,#7a7a72 0%,#a79f92 35%,#c9c0b2 60%,#8c8a86 100%)}
.hero-photo{left:430px;top:0;width:700px;height:590px;background:radial-gradient(ellipse at 60% 45%,#c7a58a 0%,#6d6561 45%,rgba(90,90,90,0) 75%)}
.hero h1{left:92px;top:232px;font-family:"Roboto Condensed",sans-serif;font-weight:700;font-size:66px;color:#fff;text-shadow:0 2px 6px rgba(0,0,0,.3)}
.hero .sub{left:92px;top:308px;font-family:"Roboto Condensed",sans-serif;font-size:33px;color:#fff}
.hero .watch{left:92px;top:381px;display:flex;align-items:center;gap:14px;font-family:"Poppins",sans-serif;font-size:17px;color:#fff}
.hero .dots{left:1178px;top:225px;display:flex;flex-direction:column;gap:14px}
.hero .dots i{width:8px;height:8px;border-radius:50%;background:#fff;display:block;opacity:.8}
.hero .dots i:first-child{background:var(--green);opacity:1}
.hero-wave{left:0;top:690px;width:1200px;height:70px}

/* what we do */
.services{left:0;top:754px;width:1200px;height:728px;background:linear-gradient(180deg,#fff 0%,#f4f4f4 100%)}
.section-title{font-family:"Poppins",sans-serif;font-weight:500;font-size:34px;width:1200px;text-align:center;left:0}
.services .section-title{top:100px}
.services .portrait{left:451px;top:206px;width:308px;height:424px;border-radius:154px 154px 20px 20px;background:linear-gradient(180deg,#e7e2de 0%,#b58b76 45%,#3c4d6b 100%)}
.svc{width:300px;font-size:14px;line-height:1.55;color:var(--grey-text)}
.svc h3{font-family:"Poppins",sans-serif;font-weight:500;font-size:18px;color:#222;margin-bottom:8px}
.svc.left{padding-left:66px}
.svc.right{text-align:right;padding-right:66px}
.svc svg{position:absolute;top:0}
.svc.left svg{left:0}
.svc.right svg{right:0}

/* online course */
.course-band{left:0;top:1482px;width:1200px;height:410px;background:var(--green-deep)}
.course-band .section-title{top:96px;color:#fff}
.card{top:1700px;width:300px;height:351px;background:#fff;box-shadow:0 6px 14px rgba(0,0,0,.15);text-align:center}
.card .thumb{width:300px;height:192px;position:relative}
.card h4{font-family:"Poppins",sans-serif;font-weight:500;font-size:19px;margin:22px 0 12px}
.card p{font-size:13px;line-height:1.7;color:#666;padding:0 28px}
.card .more{display:block;margin-top:12px;font-size:13px;font-family:"Poppins",sans-serif;color:#333}
.card.featured{background:var(--green)}
.card.featured h4,.card.featured p,.card.featured .more{color:#fff}
.play{position:absolute;left:50%;top:50%;transform:translate(-50%,-50%)}

.player{left:215px;top:2097px;width:772px;height:398px;border:5px solid var(--green);background:linear-gradient(120deg,#3b3028 0%,#7a5a3c 40%,#a97d52 65%,#3e3e44 100%);box-shadow:0 16px 24px rgba(0,0,0,.2)}

/* instructor */
.instructor{left:0;top:2602px;width:1200px;height:531px;background:linear-gradient(180deg,#f3f3f3,#ececec)}
.instructor .section-title{top:76px}
.inst-photo{left:226px;top:2833px;width:200px;height:210px;border:7px solid var(--green);background:linear-gradient(180deg,#e8e8e8 0%,#c49c83 35%,#252a3a 75%)}
.inst-body{left:477px;top:2833px;width:580px}
.inst-body h3{font-family:"Poppins",sans-serif;font-weight:500;font-size:18px;margin-bottom:10px}
.inst-body p{font-size:13px;line-height:2;color:#555}
.btn{display:inline-block;margin-top:16px;background:var(--green);color:#fff;font-family:"Poppins",sans-serif;font-size:14px;padding:6px 24px;border-radius:16px}
.arrow{top:2902px}

/* partners */
.partners{left:118px;top:3256px;width:964px;display:flex;justify-content:space-between;align-items:center}
.partners i{display:block;background:#3a3a3a;opacity:.8}

/* footer */
.footer-wave{left:0;top:3430px;width:1200px;height:90px}
.footer{left:0;top:3500px;width:1200px;height:346px;background:var(--black);color:#ddd}
.fcol{top:72px;font-size:13px}
.fcol h5{font-family:"Poppins",sans-serif;font-weight:500;font-size:14px;color:#fff;margin-bottom:18px;letter-spacing:.3px}
.fcol li{list-style:none;line-height:2.1}
.fcol li::before{content:"» ";}
.fcontact div{display:flex;align-items:center;gap:12px;margin-bottom:14px}
.subscribe{margin-top:18px;width:218px;height:42px;border:1px solid #ccc;border-radius:21px;display:flex;align-items:center;justify-content:space-between;padding:0 14px 0 20px;color:#aaa;font-size:13px}
.fsocial{display:flex;gap:14px}
.fsocial i{width:24px;height:24px;background:#fff;border-radius:3px;display:block}
.copyright{left:92px;top:290px;font-size:13px;color:#ccc}
.livechat{left:949px;top:268px;width:159px;height:51px;background:#fff;border-radius:26px;display:flex;align-items:center;justify-content:center;gap:10px;font-family:"Poppins",sans-serif;font-weight:600;font-size:18px;color:#111}
</style>
</head>
<body>

<div class="abs topbar">
  <div class="abs contact">
    <span><svg width="14" height="14" viewBox="0 0 24 24"><path fill="#ddd" d="M6.6 10.8a15 15 0 006.6 6.6l2.2-2.2c.3-.3.7-.4 1-.2 1.1.4 2.3.6 3.6.6.6 0 1 .4 1 1V20c0 .6-.4 1-1 1A17 17 0 013 4c0-.6.4-1 1-1h3.5c.6 0 1 .4 1 1 0 1.3.2 2.5.6 3.6.1.3 0 .7-.2 1z"/></svg>+49 (0) 150/2048816</span>
    <span><svg width="15" height="12" viewBox="0 0 24 18"><rect x="1" y="1" width="22" height="16" fill="#ddd"/><path d="M1 1l11 9 11-9" stroke="#2a2a2a" stroke-width="2" fill="none"/></svg>hello@learnharbor-mail.com</span>
  </div>
  <div class="abs login">Login</div>
  <div class="abs social"><i></i><i></i><i></i><i></i></div>
</div>

<header class="abs header">
  <div class="abs brand"><b></b>LearnHarbor</div>
  <nav class="abs nav">
    <span class="active">Home</span><span>About</span><span>Services</span><span>Course</span><span>Instructor</span><span>Contact</span>
  </nav>
</header>

<section class="abs hero">
  <div class="abs hero-photo" role="img" aria-label="Photo of a smiling student wearing headphones using a tablet"></div>
  <h1 class="abs">LearnHarbor</h1>
  <div class="abs sub">Neque porro quisquam dolorem</div>
  <div class="abs watch"><svg width="28" height="28" viewBox="0 0 28 28"><circle cx="14" cy="14" r="14" fill="#8cc43c"/><path d="M11 8l9 6-9 6z" fill="#fff"/></svg>WATCH VIDEO</div>
  <div class="abs dots"><i></i><i></i><i></i><i></i></div>
</section>
<svg class="abs hero-wave" viewBox="0 0 1200 70" preserveAspectRatio="none"><path d="M0 70 L0 58 Q300 38 600 52 T1200 20 L1200 70Z" fill="#fff"/></svg>

<section class="abs services">
  <h2 class="abs section-title">WHAT WE DO</h2>
  <div class="abs portrait" role="img" aria-label="Photo of a smiling student sitting cross-legged with a laptop, giving a thumbs up"></div>

  <div class="abs svc left" style="left:138px;top:262px">
    <svg width="52" height="46" viewBox="0 0 52 46" fill="none" stroke="#8cc43c" stroke-width="2.5"><rect x="3" y="3" width="46" height="30" rx="2"/><path d="M18 43h16M26 33v10"/></svg>
    <h3>Porro quisquam</h3>Duis aute irure dolor in reprehenderit in voluptate. Excepteur sint occaecat.
  </div>
  <div class="abs svc left" style="left:138px;top:454px">
    <svg width="40" height="54" viewBox="0 0 40 54" fill="none" stroke="#8cc43c" stroke-width="2.5"><rect x="6" y="2" width="28" height="50" rx="4"/><path d="M6 10h28M6 42h28"/><circle cx="20" cy="47" r="1.5"/></svg>
    <h3>Dolorem ipsum</h3>Duis aute irure dolor in reprehenderit in voluptate. Excepteur sint occaecat.
  </div>
  <div class="abs svc right" style="left:762px;top:262px">
    <svg width="46" height="50" viewBox="0 0 46 50" fill="none" stroke="#8cc43c" stroke-width="2.5"><circle cx="10" cy="25" r="7"/><circle cx="36" cy="10" r="7"/><circle cx="36" cy="40" r="7"/><path d="M16 22l14-9M16 28l14 9"/></svg>
    <h3>Neque porro</h3>Duis aute irure dolor in reprehenderit in voluptate. Excepteur sint occaecat.
  </div>
  <div class="abs svc right" style="left:762px;top:454px">
    <svg width="42" height="52" viewBox="0 0 42 52" fill="none" stroke="#8cc43c" stroke-width="2.5"><path d="M4 2h24l10 10v38H4z"/><path d="M28 2v10h10M11 24h20M11 32h20M11 40h14"/></svg>
    <h3>Quisquam porro</h3>Duis aute irure dolor in reprehenderit in voluptate. Excepteur sint occaecat.
  </div>
</section>

<section class="abs course-band">
  <h2 class="abs section-title">ONLINE COURSE</h2>
</section>

<article class="abs card" style="left:118px">
  <div class="thumb" role="img" aria-label="Photo of hands holding a tablet showing an online course" style="background:linear-gradient(135deg,#d9d4cf,#8a8580 60%,#4f6d8c)">
    <svg class="play" width="44" height="44" viewBox="0 0 44 44"><circle cx="22" cy="22" r="21" fill="#fff" opacity=".9"/><path d="M18 13l13 9-13 9z" fill="#333"/></svg>
  </div>
  <h4>Neque quisquam</h4>
  <p>The point of using Lorem Ipsum is that it has a more-or-less normal distribu-</p>
  <span class="more">Read More ▸</span>
</article>
<article class="abs card featured" style="left:454px">
  <div class="thumb" role="img" aria-label="Photo of a student working on a laptop" style="background:linear-gradient(135deg,#7a5c3f,#3a3a40 55%,#a58562)">
    <svg class="play" width="44" height="44" viewBox="0 0 44 44"><circle cx="22" cy="22" r="21" fill="#fff" opacity=".9"/><path d="M18 13l13 9-13 9z" fill="#333"/></svg>
  </div>
  <h4>Dolorem ipsum</h4>
  <p>The point of using Lorem Ipsum is that it has a more-or-less normal distribu-</p>
  <span class="more">Read More ▸</span>
</article>
<article class="abs card" style="left:787px">
  <div class="thumb" role="img" aria-label="Photo of a student studying at a laptop in a bright room" style="background:linear-gradient(135deg,#e9e7e3,#a7a29c 55%,#3f4650)">
    <svg class="play" width="44" height="44" viewBox="0 0 44 44"><circle cx="22" cy="22" r="21" fill="#fff" opacity=".9"/><path d="M18 13l13 9-13 9z" fill="#333"/></svg>
  </div>
  <h4>Porro quisquam</h4>
  <p>The point of using Lorem Ipsum is that it has a more-or-less normal distribu-</p>
  <span class="more">Read More ▸</span>
</article>

<div class="abs player" role="img" aria-label="Video player showing a lesson with a student typing on a laptop">
  <svg class="play" width="80" height="80" viewBox="0 0 80 80"><circle cx="40" cy="40" r="38" fill="#fff" opacity=".85"/><path d="M32 24l24 16-24 16z" fill="#2d5a9a"/></svg>
</div>

<section class="abs instructor">
  <h2 class="abs section-title">INSTRUCTOR</h2>
</section>
<svg class="abs arrow" style="left:92px" width="22" height="36" viewBox="0 0 22 36"><path d="M18 2L4 18l14 16" stroke="#333" stroke-width="2.5" fill="none"/></svg>
<svg class="abs arrow" style="left:1090px" width="22" height="36" viewBox="0 0 22 36"><path d="M4 2l14 16L4 34" stroke="#333" stroke-width="2.5" fill="none"/></svg>
<div class="abs inst-photo" role="img" aria-label="Portrait photo of the instructor with arms crossed"></div>
<div class="abs inst-body">
  <h3>Neque porro quisquam</h3>
  <p>It is a long established fact that a reader will be distracted by the readable content of a page when looking at its layout. The point of using Lorem Ipsum is that it has a more-or-less normal distribution of letters, as opposed to using 'Content here, content here', making it look like readable English. Many desktop publishing packages and web page editors now use Lorem Ipsum as their default model text.</p>
  <span class="btn">Read More</span>
</div>

<div class="abs partners" aria-label="Partner badges">
  <i style="width:90px;height:56px;border-radius:4px"></i>
  <i style="width:96px;height:40px;border-radius:4px"></i>
  <i style="width:72px;height:72px;border-radius:50%"></i>
  <i style="width:100px;height:48px;border-radius:24px"></i>
  <i style="width:86px;height:60px;border-radius:4px"></i>
  <i style="width:96px;height:44px;border-radius:4px"></i>
  <i style="width:84px;height:60px;clip-path:polygon(0 0,100% 0,50% 100%)"></i>
</div>

<svg class="abs footer-wave" viewBox="0 0 1200 90" preserveAspectRatio="none">
  <path d="M0 90 L0 38 Q300 0 600 30 T1200 22 L1200 90Z" fill="#8cc43c"/>
  <path d="M0 90 L0 50 Q300 12 600 42 T1200 34 L1200 90Z" fill="#050505"/>
</svg>

<footer class="abs footer">
  <div class="abs fcol" style="left:92px">
    <h5>INFORMATION</h5>
    <ul><li>Privacy Policy</li><li>Your Account</li><li>Advanced Search</li><li>Contact Us</li></ul>
  </div>
  <div class="abs fcol fcontact" style="left:318px">
    <h5>CONTACT US</h5>
    <div><svg width="22" height="22" viewBox="0 0 22 22"><circle cx="11" cy="11" r="11" fill="#fff"/><path d="M11 5a4 4 0 00-4 4c0 3 4 8 4 8s4-5 4-8a4 4 0 00-4-4z" fill="#050505"/></svg>214 Orchard Lane, Fernvale WA 98120</div>
    <div><svg width="22" height="22" viewBox="0 0 22 22"><circle cx="11" cy="11" r="11" fill="#fff"/><path d="M8 6l2 3-1 1a7 7 0 003 3l1-1 3 2-1 2c-4 0-9-5-9-9z" fill="#050505"/></svg>509-410-7782</div>
    <div><svg width="22" height="22" viewBox="0 0 22 22"><circle cx="11" cy="11" r="11" fill="#fff"/><rect x="6" y="7.5" width="10" height="7" fill="#050505"/></svg>hello@learnharbor-mail.com</div>
  </div>
  <div class="abs fcol" style="left:656px;width:230px">
    <h5>JOIN OUR MAILING LIST</h5>
    <p style="line-height:1.6">Your about us information would fit here nicely.</p>
    <div class="subscribe">Email address<svg width="16" height="16" viewBox="0 0 16 16"><circle cx="8" cy="8" r="8" fill="#ccc"/><path d="M8 4v8M4 8h8" stroke="#050505" stroke-width="2"/></svg></div>
  </div>
  <div class="abs fcol" style="left:949px">
    <h5>FOLLOW US OUT THERE</h5>
    <div class="fsocial"><i></i><i></i><i></i><i></i></div>
  </div>
  <div class="abs copyright">Copyright © 2018. All Rights Reserved</div>
  <div class="abs livechat"><svg width="26" height="24" viewBox="0 0 26 24"><path d="M3 3h20v13H10l-5 5v-5H3z" fill="none" stroke="#111" stroke-width="2.2"/></svg>Live Chat</div>
</footer>

</body>
</html>
```